Website for Boutique Property Consultancy in UK

We are looking to designing a website for our Property Consultancy Services that follows a minimalistic clean style that is also bold and intriguing.
The website will be based on one landing page and a link to LinkedIn Page and email link.

Dominant features will be the company logo or icon and colours.

Brand colours provided for guidance.

Looking to achieve a minimalistic clean style that is also bold and intriguing.

"Updated"
Page 1 - Landing Page with the Hyperlinks to Pick a Service, Training Portal and Maple Nine Portal. example landing page https://tilbrook-studio.co.uk/

Page 2 - Shows all the Services and Sectors

Target Market(s)

Occupier Clients, Tech Companies, Property Developers, Infrastructure Clients and Major Consultants

Industry/Entity Type

Construction

Coding

Coded - Design and coding required

Number of Pages Required

2 page

Font styles to use
Other font styles liked:
• Century Gothic or Futuris (Headings)

Colors
0054AA
0677BA
7BADD7
CADEEF
E8F1F8
00AB8E
00BBA5
67D7C9
C6EFE9
E9F9F6

Requirements
Must have
• Company Logo, link to enquiry and LinkedIn

```html
<!DOCTYPE html>
<html lang="en">
<head>
<meta charset="utf-8">
<title>Fenwick Oake — Property Consultancy</title>
<link href="https://fonts.googleapis.com/css2?family=Urbanist:wght@300;400;500;700;800&display=swap" rel="stylesheet">
<style>
  :root {
    --page-bg: #f2f2f3;
    --surface: #ffffff;
    --ink: #2b2f4c;
    --ink-soft: #3a3d52;
    --rule: #dedfe3;
    --footer: #2d3150;
    --footer-text: #e6e7ee;
    --accent-green: #1fb574;
    --sky-pink: #f3d3da;
    --sky-blue: #d3dde4;
  }
  * { box-sizing: border-box; margin: 0; padding: 0; }
  html, body { width: 1022px; height: 1200px; overflow: hidden; }
  body {
    background: var(--page-bg);
    font-family: "Urbanist", "Century Gothic", sans-serif;
    color: var(--ink);
    position: relative;
  }
  .site {
    position: absolute;
    left: 21px; top: 304px;
    width: 980px; height: 592px;
    background: var(--surface);
    box-shadow: 0 10px 30px rgba(0,0,0,0.18);
    overflow: hidden;
  }
  .site-header {
    position: absolute; left: 0; top: 0; width: 100%; height: 117px;
    border-bottom: 1px solid var(--rule);
  }
  .site-header .cell-left, .site-header .cell-right {
    position: absolute; top: 0; height: 100%;
  }
  .site-header .cell-left { left: 0; width: 227px; border-right: 1px solid var(--rule); }
  .site-header .cell-right { right: 0; width: 248px; border-left: 1px solid var(--rule); }
  .brand {
    position: absolute; left: 227px; width: 505px; top: 0; height: 117px;
    display: flex; align-items: center; justify-content: center;
    font-size: 50px; font-weight: 700; letter-spacing: 0.5px;
    color: var(--ink); text-decoration: none;
  }
  .skyline {
    position: absolute; left: 0; top: 297px; width: 100%; height: 235px;
    background:
      linear-gradient(to bottom, rgba(255,255,255,1) 0%, rgba(255,255,255,0.2) 45%, rgba(255,255,255,0) 80%, rgba(255,255,255,0.5) 100%),
      linear-gradient(to right, var(--sky-pink) 0%, #f6e2e6 45%, #e4e6ec 65%, var(--sky-blue) 100%);
  }
  .hero {
    position: absolute; left: 0; top: 180px; width: 100%; text-align: center;
  }
  .hero-title { font-size: 34px; line-height: 38px; color: var(--ink-soft); font-weight: 400; letter-spacing: 1px; }
  .hero-title strong { display: block; font-weight: 800; color: var(--ink); letter-spacing: 1.2px; }
  .portal-nav {
    position: absolute; top: 305px; left: 0; width: 100%;
    display: flex; justify-content: center; align-items: center;
  }
  .portal-link {
    display: flex; align-items: center; gap: 14px;
    font-size: 17px; font-weight: 400; color: var(--ink); text-decoration: none;
    padding: 0 22px;
  }
  .portal-link svg { width: 12px; height: 12px; }
  .portal-divider { width: 1px; height: 30px; background: var(--ink); }
  .enquiry-button {
    position: absolute; left: 881px; top: 445px; width: 54px; height: 54px;
    border-radius: 50%; background: #fff;
    box-shadow: 0 3px 10px rgba(0,0,0,0.18);
    display: flex; align-items: center; justify-content: center;
  }
  .site-footer {
    position: absolute; left: 0; bottom: 0; width: 100%; height: 60px;
    background: var(--footer); color: var(--footer-text);
    display: flex; align-items: center; justify-content: space-between;
    padding: 0 66px;
  }
  .copyright { font-size: 12px; }
  .footer-links { display: flex; align-items: center; gap: 20px; }
  .footer-links a { display: flex; }
  .social-mark { width: 14px; height: 14px; border-radius: 50%; background: var(--footer-text); }
  .member-badge { width: 50px; height: 16px; border-radius: 3px; background: var(--footer-text); }
</style>
</head>
<body>
  <div class="site">
    <header class="site-header">
      <div class="cell-left"></div>
      <a class="brand" href="#">Fenwick Oake</a>
      <div class="cell-right"></div>
    </header>

    <div class="skyline" role="img" aria-label="Faint city skyline of towers fading from soft pink to pale blue-grey"></div>

    <section class="hero">
      <h1 class="hero-title">Delivering Value and <strong>Redefining Boundaries</strong></h1>
    </section>

    <nav class="portal-nav">
      <a class="portal-link" href="#">Pick a services
        <svg viewBox="0 0 12 12" fill="none" stroke="currentColor" stroke-width="1.4"><path d="M1 6h10M7 2l4 4-4 4"/></svg></a>
      <span class="portal-divider"></span>
      <a class="portal-link" href="#">Training Portal
        <svg viewBox="0 0 12 12" fill="none" stroke="currentColor" stroke-width="1.4"><path d="M1 6h10M7 2l4 4-4 4"/></svg></a>
      <span class="portal-divider"></span>
      <a class="portal-link" href="#">Maple Nine Portal
        <svg viewBox="0 0 12 12" fill="none" stroke="currentColor" stroke-width="1.4"><path d="M1 6h10M7 2l4 4-4 4"/></svg></a>
    </nav>

    <a class="enquiry-button" href="#" aria-label="Send an enquiry">
      <svg width="22" height="16" viewBox="0 0 22 16"><rect width="22" height="16" rx="2.5" fill="var(--accent-green)"/><path d="M2 3l9 6 9-6" fill="none" stroke="#fff" stroke-width="1.8"/></svg>
    </a>

    <footer class="site-footer">
      <p class="copyright">© fenwickoake. All Rights Reserved</p>
      <div class="footer-links">
        <a href="#" aria-label="Email">
          <svg width="16" height="13" viewBox="0 0 16 13" fill="none" stroke="var(--footer-text)" stroke-width="1.3"><rect x="0.7" y="0.7" width="14.6" height="11.6" rx="2"/><path d="M1.5 2l6.5 5 6.5-5"/></svg>
        </a>
        <a href="#" aria-label="Professional network"><span class="social-mark"></span></a>
        <span class="member-badge" aria-label="Professional membership"></span>
      </div>
    </footer>
  </div>
</body>
</html>
```